Premium Food Label Design – High-End Boutique Jar Labels (3 Sizes)

I require a complete jar label redesign across three sizes:
75mm x 130mm (Large & Medium)
55mm x 120mm (Small)
45mm x 120mm (XS)

The design must feel professional, modern, elegant, and high-end boutique.
Primary aesthetic: white, minimal, refined, with accents in soft brown and gold/bronze. (see prefer colours of logo in OLD LABEL PDF)
Transparent background required.

I have attached my current label for wording reference only — I want to move away from the kraft look entirely.
The label must include all existing details, plus a dedicated space to manually add batch number and date.

IMPORTANT: Final files must be supplied as editable Adobe Illustrator (.AI) files with live text layers (not outlined) so I can update them as needed.
Logo is attached. I’m open to a fresh, elevated design direction aligned with a premium brand feel.
Updates

Low design quality

Target Market(s)

People who appreciate high-end, thoughtfully crafted food and are willing to pay for quality

Industry/Entity Type

Gourmet Food / Artisan Food Packaging

Requirements
Must have
• Premium, minimal aesthetic, Strong typography hierarchy, White background, Consistency across 3 sizes
Nice to have
• Elevated “Amber Meadow” styling
Should not have
• No bright or bold colours, No clutter or overcrowding, No heavy borders or thick frames,No “homemade/craft” fonts

```html
<!DOCTYPE html>
<html lang="en">
<head>
<meta charset="utf-8">
<title>Golden Ladle – Tomato Relish Jar Labels</title>
<link rel="stylesheet" href="https://fonts.googleapis.com/css2?family=EB+Garamond:wght@500;700&family=Libre+Baskerville:wght@400;700&family=Oswald:wght@300;400&display=swap">
<style>
  :root {
    --canvas: #f3f1ec;
    --label-white: #ffffff;
    --hairline: #e3dacb;
    --brown: #5e4838;
    --brown-soft: #7a6352;
    --ink: #2b2420;
    --gold: #c39a45;
    --gold-light: #dcbb6a;
    --bronze: #9c7230;
    --serif: "EB Garamond", Georgia, serif;
    --display: "Libre Baskerville", Georgia, serif;
    --condensed: "Oswald", "Arial Narrow", sans-serif;
  }
  * { box-sizing: border-box; margin: 0; padding: 0; }
  html, body { width: 901px; height: 1200px; overflow: hidden; background: var(--canvas); }
  .sheet { position: relative; width: 901px; height: 1200px; }

  .label {
    position: absolute;
    display: flex;
    background: var(--label-white);
    border: 1px solid var(--hairline);
    box-shadow: 0 1px 3px rgba(60,40,20,.12);
  }
  .label--large  { left: 76.5px; top: 19px;  width: 751.5px; height: 281px; }
  .label--medium { left: 76.5px; top: 330px; width: 751.5px; height: 343px; }
  .label--small  { left: 45px;   top: 703px; width: 814.5px; height: 469.5px; }

  .front { position: relative; flex: 1; color: var(--brown); }

  .intention {
    position: absolute;
    left: 0;
    text-align: center;
    font-family: var(--serif);
    font-weight: 500;
    line-height: 1;
    color: var(--brown);
  }
  .intention__title { font-weight: 700; color: var(--ink); }
  .intention__divider {
    display: block;
    margin: 2px auto;
    width: 46px;
    height: 8px;
    color: var(--gold);
  }

  .brand {
    position: absolute;
    text-align: center;
    transform: translateX(-50%);
    white-space: nowrap;
  }
  .brand__name {
    font-family: var(--display);
    font-weight: 400;
    color: var(--bronze);
    letter-spacing: .12em;
    line-height: 1;
  }
  .brand__mark {
    display: block;
    margin: 0 auto 6px;
    border-radius: 50%;
    background: var(--gold);
  }

  .product {
    position: absolute;
    transform: translateX(-50%);
    text-align: center;
    font-family: var(--display);
    font-weight: 700;
    line-height: .98;
    white-space: nowrap;
    background: linear-gradient(180deg, var(--gold-light) 0%, var(--gold) 45%, var(--bronze) 100%);
    -webkit-background-clip: text;
    background-clip: text;
    color: transparent;
  }

  .ornament {
    position: absolute;
    transform: translateX(-50%);
    border-radius: 20px;
    background: radial-gradient(ellipse at center, rgba(195,154,69,.85) 0%, rgba(195,154,69,.35) 45%, rgba(195,154,69,0) 75%);
  }

  .net-weight {
    position: absolute;
    transform: translate(-50%, -50%);
    font-family: var(--condensed);
    font-weight: 400;
    color: var(--bronze);
    white-space: nowrap;
  }

  .storage {
    font-family: var(--condensed);
    font-weight: 400;
    color: var(--ink);
    white-space: nowrap;
    letter-spacing: -.01em;
  }
  .front .storage { position: absolute; color: var(--brown); }

  .panel {
    position: relative;
    background: var(--label-white);
    border-left: 1px solid var(--hairline);
    color: var(--ink);
    font-family: var(--condensed);
    font-weight: 300;
  }
  .panel__details {
    position: absolute;
    writing-mode: vertical-rl;
    transform: rotate(180deg);
    line-height: 1.12;
    white-space: nowrap;
  }
  .panel__details p { margin: 0; }
  .panel__key { text-decoration: underline; text-underline-offset: 2px; }
  .panel__record { display: flex; justify-content: space-between; }
  .panel .storage { position: absolute; left: 6px; }

  /* Large */
  .label--large .panel { width: 141px; }
  .label--large .intention { top: 9px; width: 162px; font-size: 20px; }
  .label--large .brand { left: 373px; top: 12px; }
  .label--large .brand__name { font-size: 24px; }
  .label--large .brand__mark { width: 12px; height: 12px; }
  .label--large .product { left: 373px; top: 80px; font-size: 54px; }
  .label--large .ornament { left: 373px; top: 195px; width: 133px; height: 38px; }
  .label--large .net-weight { left: 373px; top: 255px; font-size: 21px; }
  .label--large .panel__details { left: 6px; top: 10px; bottom: 26px; width: 128px; font-size: 16px; line-height: 1.15; }
  .label--large .panel .storage { bottom: 8px; font-size: 9.5px; }

  /* Medium */
  .label--medium .panel { width: 163.5px; }
  .label--medium .intention { top: 16px; width: 168px; font-size: 22px; line-height: 1.02; }
  .label--medium .brand { left: 370px; top: 20px; }
  .label--medium .brand__name { font-size: 25px; }
  .label--medium .brand__mark { width: 13px; height: 13px; }
  .label--medium .product { left: 370px; top: 112px; font-size: 55px; }
  .label--medium .ornament { left: 370px; top: 225px; width: 146px; height: 42px; }
  .label--medium .net-weight { left: 370px; top: 314px; font-size: 22px; }
  .label--medium .panel__details { left: 4px; top: 12px; bottom: 30px; width: 156px; font-size: 20px; line-height: 1.12; }
  .label--medium .panel .storage { bottom: 10px; font-size: 11px; }

  /* Small */
  .label--small .panel { width: 122px; }
  .label--small .intention { top: 24px; width: 188px; font-size: 23px; line-height: 1.17; }
  .label--small .intention__title { margin-bottom: 26px; }
  .label--small .brand { left: 427px; top: 22px; }
  .label--small .brand__name { font-size: 31px; }
  .label--small .brand__mark { width: 15px; height: 15px; }
  .label--small .product { left: 427px; top: 160px; font-size: 67px; }
  .label--small .ornament { left: 427px; top: 310px; width: 190px; height: 56px; }
  .label--small .net-weight { left: 427px; top: 440px; font-size: 25px; }
  .label--small .front .storage { left: 8px; top: 442px; font-size: 14px; }
  .label--small .panel__details { left: 6px; top: 36px; bottom: 10px; width: 112px; font-size: 21px; line-height: 1.22; }
  .label--small .panel__record { margin-left: 8px; }
</style>
</head>
<body>
<main class="sheet">

  <!-- Large: 75 x 130 mm -->
  <section class="label label--large" aria-label="Large jar label">
    <div class="front">
      <div class="intention">
        <p class="intention__title">Amber Meadow</p>
        <p>What is made<br>with love is felt<br>in return.</p>
        <svg class="intention__divider" viewBox="0 0 46 8" aria-hidden="true"><path d="M2 4 Q12 0 23 4 Q34 8 44 4" fill="none" stroke="currentColor" stroke-width="1.2"/></svg>
        <p>May this relish<br>nourish more<br>than the meal-<br>bringing<br>comfort,<br>connection, and<br>joy to every<br>moment shared.</p>
      </div>
      <div class="brand">
        <span class="brand__mark" aria-hidden="true"></span>
        <p class="brand__name">GOLDEN LADLE</p>
      </div>
      <h1 class="product">TOMATO<br>RELISH</h1>
      <div class="ornament" role="img" aria-label="Gold engraved tomato slice flanked by flourishes"></div>
      <p class="net-weight">NET WT.: 375g</p>
    </div>
    <aside class="panel">
      <div class="panel__details">
        <p><span class="panel__key">Ingredients:</span> Tomatoes, onion, sugar, vinegar,</p>
        <p>salt, spices, thickener (cornflower)</p>
        <p>Made by: Golden Ladle, QLD, Australia</p>
        <p>goldenladle.com info@goldenladle.com</p>
        <p>DATE:</p>
        <p>BATCH#:</p>
      </div>
      <p class="storage">KEEP REFRIGERATED ONCE OPENED</p>
    </aside>
  </section>

  <!-- Medium: 55 x 120 mm -->
  <section class="label label--medium" aria-label="Medium jar label">
    <div class="front">
      <div class="intention">
        <p class="intention__title">Amber Meadow</p>
        <p>What is made<br>with love is felt<br>in return.</p>
        <svg class="intention__divider" viewBox="0 0 46 8" aria-hidden="true"><path d="M2 4 Q12 0 23 4 Q34 8 44 4" fill="none" stroke="currentColor" stroke-width="1.2"/></svg>
        <p>May this relish<br>nourish more<br>than the meal-<br>bringing<br>comfort,<br>connection, and<br>joy to every<br>moment shared.</p>
      </div>
      <div class="brand">
        <span class="brand__mark" aria-hidden="true"></span>
        <p class="brand__name">GOLDEN LADLE</p>
      </div>
      <h2 class="product">TOMATO<br>RELISH</h2>
      <div class="ornament" role="img" aria-label="Gold engraved tomato slice flanked by flourishes"></div>
      <p class="net-weight">NET WT.: 375g</p>
    </div>
    <aside class="panel">
      <div class="panel__details">
        <p><span class="panel__key">Ingredients:</span> Tomatoes, onion, sugar, vinegar,</p>
        <p>salt, spices, thickener (cornflower)</p>
        <p>Made by: Golden Ladle, QLD, Australia</p>
        <p>goldenladle.com info@goldenladle.com</p>
        <p>DATE:</p>
        <p>BATCH#:</p>
      </div>
      <p class="storage">KEEP REFRIGERATED ONCE OPENED</p>
    </aside>
  </section>

  <!-- Small: 45 x 120 mm -->
  <section class="label label--small" aria-label="Small jar label">
    <div class="front">
      <div class="intention">
        <p class="intention__title">Amber Meadow</p>
        <p>What is made<br>with love is felt<br>in return.</p>
        <svg class="intention__divider" viewBox="0 0 46 8" aria-hidden="true"><path d="M2 4 Q12 0 23 4 Q34 8 44 4" fill="none" stroke="currentColor" stroke-width="1.2"/></svg>
        <p>May this relish<br>nourish more<br>than the meal-<br>bringing<br>comfort,<br>connection, and<br>joy to every<br>moment shared.</p>
      </div>
      <div class="brand">
        <span class="brand__mark" aria-hidden="true"></span>
        <p class="brand__name">GOLDEN LADLE</p>
      </div>
      <h2 class="product">TOMATO<br>RELISH</h2>
      <div class="ornament" role="img" aria-label="Gold engraved tomato slice flanked by flourishes"></div>
      <p class="net-weight">NET WT.: 375g</p>
      <p class="storage">KEEP REFRIGERATED ONCE OPENED</p>
    </div>
    <aside class="panel">
      <div class="panel__details">
        <p><span class="panel__key">Ingredients:</span> Tomatoes, onion, sugar, vinegar, salt, spices,</p>
        <p>thickener (cornflower) <span class="panel__key">Made by:</span> Golden Ladle, QLD, Australia</p>
        <p>goldenladle.com | info@goldenladle.com</p>
        <p class="panel__record"><span>DATE:</span><span>BATCH#:</span></p>
      </div>
    </aside>
  </section>

</main>
</body>
</html>
```